We need a web design for a retail food business based in Greater Western Sydney Australia called Golden Lantern Chinese Restaurant. Basically just need a simple yet easily to navigate website to browse through a menu, gallery , brief description about us, opening hours.
Menu and Gallery will be constantly updated.
Will provide own images for gallery
Updates
Menu has been uploaded and some idea on the colours I would like on the site
Some additional pictures added to see what designs you guys can come up with . Thanks again
To All Designers,
Any extra fee on top of the designs that feels need to be charged, please let me know in advance
Reason: Extending Deadline as I have yet to find a design that I would like...Thanks guys
Target Market(s)
All groups
Industry/Entity Type
Business
Requirements
Must have
- Open minded to any designs
Nice to have
- Would like slideshow behind main logo.
Preferred light coloured site yet not too playful
Should not have
- Preferably no dark colours backgrounds

```html
<!DOCTYPE html>
<html lang="en">
<head>
<meta charset="utf-8">
<title>Golden Lantern Chinese Restaurant</title>
<link rel="stylesheet" href="https://fonts.googleapis.com/css2?family=Figtree:ital,wght@0,400;0,600;0,700;0,800;1,400;1,600;1,700&display=swap">
<style>
:root{
  --brick:#a9402c;
  --brick-dark:#8f3222;
  --orange:#e8802c;
  --ink:#2b2b2b;
  --board:#1c1513;
  --cream:#fff;
  --dot:#c9c4be;
}
*{box-sizing:border-box;margin:0;padding:0}
html,body{width:847px;height:1200px;overflow:hidden}
body{position:relative;background:var(--cream);font-family:"Figtree",sans-serif;color:var(--ink)}
.abs{position:absolute}

/* header */
.header{left:0;top:0;width:847px;height:58px;background:#fff;border-bottom:1px solid #e6e0da}
.brand{left:86px;top:14px;font-weight:800;font-size:19px;color:var(--brick);letter-spacing:.3px;line-height:1}
.brand-mark{display:inline-block;width:10px;height:10px;border-radius:50%;background:var(--brick);margin-right:6px;vertical-align:1px}
.nav{left:384px;top:24px;display:flex;gap:28px;font-size:10.5px;font-weight:600;color:#333}
.nav a{color:inherit;text-decoration:none}
.nav .active{color:var(--brick);border-bottom:2px solid var(--brick);padding-bottom:3px}
.social-top{left:720px;top:19px;display:flex;gap:10px}
.social-top span{width:18px;height:18px;border-radius:50%;background:var(--orange)}

/* hero */
.hero{left:0;top:58px;width:847px;height:331px;background:linear-gradient(135deg,#4a3430 0%,#6b3a2e 35%,#8a5540 55%,#3a2422 100%)}
.tagline{left:86px;top:63px;color:#fff;font-weight:600;font-size:12px;letter-spacing:.3px}
.phone-box{left:566px;top:50px;width:202px;height:39px;background:var(--brick);border:2px solid #fff;border-top:none;border-radius:0 0 4px 4px;color:#fff;font-weight:600;font-size:21px;display:flex;align-items:center;justify-content:center;gap:8px}
.hero-kicker{left:90px;top:196px;color:#fff;font-size:20px;font-weight:600}
.hero-title{left:92px;top:226px;color:#fff;font-family:"Figtree",sans-serif;font-weight:700;font-size:50px;line-height:1;letter-spacing:3px}
.dots{left:378px;top:362px;width:92px;height:27px;background:#efe9e3;border-radius:6px 6px 0 0;display:flex;gap:5px;justify-content:center;align-items:center}
.dots i{width:10px;height:10px;border-radius:50%;background:#fff;border:1px solid #bbb}
.dots i.on{background:var(--brick);border-color:var(--brick)}

/* specialities */
.sec-title{font-weight:700;font-size:16px;color:var(--brick);letter-spacing:.3px}
.dish{width:200px}
.dish h3{font-size:12.5px;font-weight:600;color:var(--brick);line-height:1.25}
.dish small{display:block;font-style:italic;font-size:8.5px;color:var(--brick)}
.dish p{width:184px;margin-top:14px;font-size:9px;line-height:17px;color:#333}
.price{width:50px;height:50px;border-radius:50%;background:var(--brick);color:#fff;font-weight:700;font-style:italic;font-size:19px;display:flex;align-items:center;justify-content:center;box-shadow:2px 3px 0 #e6dcd6}
.price sup{font-size:10px}
.vline{left:304px;top:478px;height:262px;border-left:2px dotted var(--dot)}
.hline{border-top:2px dotted var(--dot)}

/* hours board */
.hanger{left:630px;top:468px}
.board{left:581px;top:499px;width:161px;height:226px;background:var(--board);border:3px solid var(--brick);border-radius:6px;color:#fff;text-align:center;padding-top:14px}
.board em{display:block;font-size:12px;font-style:italic}
.board b{display:block;font-size:16px;font-weight:700;margin-top:4px}
.board p{font-size:11.5px;line-height:15px}
.board .small-b{font-size:12.5px}

.btn{left:349px;top:771px;width:150px;height:33px;background:var(--brick);color:#fff;font-weight:700;font-size:12.5px;letter-spacing:.5px;display:flex;align-items:center;justify-content:center}

/* gallery */
.thumb{top:875px;width:97px;height:69px;border:2px solid #e8a08a;border-radius:2px}
.more{left:666px;top:876px;width:108px;text-align:center}
.more .a{font-size:16px;font-weight:700;font-style:italic;color:#222}
.more .b{font-size:12px;letter-spacing:7px;margin-top:3px}
.more .c{font-size:20px;font-weight:700;color:var(--brick);border-bottom:1px solid var(--brick);display:inline-block;line-height:1.1}

/* footer */
.footer{left:0;top:1009px;width:847px;height:191px;background:var(--brick);color:#fff}
.f-links{left:78px;top:1036px;font-size:11px;line-height:20.5px;letter-spacing:.3px}
.f-hours{left:210px;top:1036px;font-size:11px;letter-spacing:.3px}
.f-hours p{font-weight:700;font-size:9.5px;margin-top:12px}
.f-hours p+p{margin-top:9px}
.f-sign{left:433px;top:1036px;font-size:11px;line-height:12px;letter-spacing:.3px}
.field{width:142px;height:21px;background:#fff;border-radius:3px;color:#aaa;font-style:italic;font-size:9.5px;padding:5px 8px}
.submit{left:433px;top:1129px;width:53px;height:21px;background:var(--brick-dark);font-size:10.5px;display:flex;align-items:center;justify-content:center;border:1px solid #6e2417}
.f-contact{left:636px;top:1036px;font-size:11px;letter-spacing:.3px}
.f-contact .tel{font-size:11.5px;font-weight:600;margin-top:10px;padding-left:24px}
.f-contact .addr{font-size:9px;line-height:17px;margin-top:7px;padding-left:26px}
.f-contact .note{font-size:7px;margin-top:3px}
.social-foot{left:78px;top:1151px;display:flex;gap:5px}
.social-foot span{width:23px;height:23px;border-radius:50%;background:#fff}
.copy{left:0;top:1176px;width:847px;text-align:center;font-size:9px}
</style>
</head>
<body>

<header class="abs header">
  <div class="abs brand"><span class="brand-mark"></span>GOLDEN LANTERN</div>
  <nav class="abs nav">
    <a class="active">HOME</a><a>MENU</a><a>ABOUT US</a><a>GALLERY</a><a>CONTACT</a>
  </nav>
  <div class="abs social-top"><span></span><span></span></div>
</header>

<section class="abs hero" role="img" aria-label="Slideshow photo of dumplings and san choy bow on a wooden board with a decorative ribbon"></section>
<div class="abs tagline">LICENSED CHINESE RESTAURANT</div>
<div class="abs phone-box">
  <svg width="18" height="18" viewBox="0 0 24 24" aria-hidden="true"><path d="M6.6 10.8a15 15 0 0 0 6.6 6.6l2.2-2.2c.3-.3.7-.4 1-.2 1.1.4 2.3.6 3.6.6.6 0 1 .4 1 1V20c0 .6-.4 1-1 1A17 17 0 0 1 3 4c0-.6.4-1 1-1h3.5c.6 0 1 .4 1 1 0 1.3.2 2.5.6 3.6.1.3 0 .7-.2 1z" fill="#fff"/></svg>
  (02) 4710 5582
</div>
<div class="abs hero-kicker">Speciality of the house</div>
<div class="abs hero-title">SAN CHOY BOW</div>
<div class="abs dots"><i class="on"></i><i></i><i></i><i></i><i></i></div>

<h2 class="abs sec-title" style="left:78px;top:420px">OUR SPECIALITIES</h2>
<h2 class="abs sec-title" style="left:569px;top:420px">WE ARE OPEN 7 DAYS !</h2>

<div class="abs price" style="left:243px;top:467px">14.<sup>80</sup></div>
<div class="abs dish" style="left:91px;top:497px">
  <h3>SAN CHOY BOW</h3>
  <p>A mixture of finely minced pork, water chester nuts, mushrooms and bamboo shoots cooked with a touch of garlic and served with selected lettuce leaves.</p>
</div>

<div class="abs price" style="left:480px;top:467px">11.<sup>80</sup></div>
<div class="abs dish" style="left:328px;top:497px">
  <h3>PEEK GAI TOD</h3><small>(6 pieces per serve)</small>
  <p>Marinated chicken wings,fried and served with sweet cilli sauce</p>
</div>

<div class="abs vline"></div>
<div class="abs hline" style="left:88px;top:601px;width:440px"></div>

<div class="abs price" style="left:243px;top:616px">16.<sup>80</sup></div>
<div class="abs dish" style="left:91px;top:646px">
  <h3>SINGAPORE SEAFOOD<br>SAN CHOY BOW</h3>
  <p>Mixed seafood dices cooked in chilli and served with lettuce leave.</p>
</div>

<div class="abs price" style="left:480px;top:616px">18.<sup>80</sup></div>
<div class="abs dish" style="left:328px;top:646px">
  <h3>WASABI STEAK</h3>
  <p>Tender steak marinated with wasabi and mayonaise sauce and pan fried.</p>
</div>

<svg class="abs hanger" width="62" height="32" viewBox="0 0 62 32" aria-hidden="true">
  <path d="M2 31 L31 3 L60 31" fill="none" stroke="#222" stroke-width="2.5"/>
  <circle cx="31" cy="5" r="3.5" fill="var(--brick)"/>
</svg>
<div class="abs board">
  <em>Lunch</em>
  <b>MON - FRI</b>
  <p>11:30 AM - 3 PM</p>
  <em style="margin-top:22px">Dinner</em>
  <b class="small-b" style="margin-top:12px">SUN, MON, TUE, WED<br>&amp; PUBLIC HOLIDAYS</b>
  <p>5 PM - 9:30 PM</p>
  <b class="small-b" style="margin-top:9px">THU, FRI &amp; SAT</b>
  <p>5 PM - 10:30 PM</p>
</div>

<div class="abs btn">VIEW FULL MENU</div>

<div class="abs hline" style="left:78px;top:851px;width:700px"></div>
<div class="abs thumb" style="left:78px;background:linear-gradient(135deg,#dfe8d0,#6f9a48,#c23a2a)" role="img" aria-label="Gallery photo of lettuce cups with sauce"></div>
<div class="abs thumb" style="left:197px;background:linear-gradient(135deg,#4e5e3c,#a4b27c,#6c7a4c)" role="img" aria-label="Gallery photo of san choy bow in lettuce leaf"></div>
<div class="abs thumb" style="left:315px;background:linear-gradient(135deg,#2a1f1a,#5e8a2e,#3a2a22)" role="img" aria-label="Gallery photo of glazed meat with greens"></div>
<div class="abs thumb" style="left:434px;background:linear-gradient(135deg,#d8d4cc,#7a4a2a,#c9c3b6)" role="img" aria-label="Gallery photo of stir-fried chicken on a plate"></div>
<div class="abs thumb" style="left:552px;background:linear-gradient(135deg,#8a3b2a,#c7a083,#3d2b22)" role="img" aria-label="Gallery photo of minced pork in a bowl"></div>
<div class="abs more">
  <div class="a">VIEW MORE</div>
  <div class="b">IN THE</div>
  <div class="c">GALLERY</div>
</div>
<div class="abs hline" style="left:78px;top:967px;width:700px"></div>

<footer class="abs footer"></footer>
<div class="abs f-links" style="color:#fff">Menu<br>About Us<br>Galery<br>Contact Us</div>
<div class="abs f-hours" style="color:#fff">Opening hours
  <p>MON - FRI : 9PM to 5PM</p><p>SAT : 10PM to 2PM</p><p>SUN : CLOSED</p>
</div>
<div class="abs f-sign" style="color:#fff">Sign up<br>for news and deals</div>
<div class="abs field" style="left:433px;top:1071px">name</div>
<div class="abs field" style="left:433px;top:1099px">email</div>
<div class="abs submit" style="color:#fff">SUBMIT</div>
<div class="abs f-contact" style="color:#fff">Contact us
  <div class="tel" style="position:relative">
    <svg style="position:absolute;left:0;top:0" width="15" height="13" viewBox="0 0 24 20" aria-hidden="true"><path d="M2 6c0-3 20-3 20 0v2h-5V6H7v2H2zM5 9h14l2 10H3zM12 11a3 3 0 1 0 .01 0z" fill="#fff"/></svg>
    (02) 4710 5582</div>
  <div class="addr" style="position:relative">
    <svg style="position:absolute;left:2px;top:2px" width="10" height="14" viewBox="0 0 10 14" aria-hidden="true"><path d="M5 0a5 5 0 0 1 5 5c0 4-5 9-5 9S0 9 0 5a5 5 0 0 1 5-5zm0 3a2 2 0 1 0 .01 0z" fill="#fff"/></svg>
    Shop 5<br>9-11 Harbour Walk<br>Kingsbury NSW 2761</div>
  <div class="note">(Turn right over Willow Creek Bridge)</div>
</div>
<div class="abs social-foot"><span></span><span></span><span></span></div>
<div class="abs copy" style="color:#fff">© Copyright 2013 Golden Lantern. All Rights Reserved.</div>

</body>
</html>
```